Playful, fun, and futuristic Call for Papers for a conference on VR/AR/MR for education and training

Create TWO versions containing the text from each of the attached Word files:
a) Short version: One ledger-sized page, edge-to-edge (no margins)
b) Long version: Between two and four letter-sized pages, edge-to-edge (no margins)

The design should:

1. resonate with/reflect the conference theme (MOST IMPORTANT) -- future focus, clear vision, blurring of boundaries between physical and virtual;

2. make a subtle nod to the venue of the conference (San Luis Obispo, California) -- e.g., silhouette of iconic landmarks (lighthouse and/or castle) / landscape and architecture of the city. (Please Google "San Luis Obispo" if you are not familiar with it);

3. be playful, fun, and futuristic, but not cliched;

4. prominently display the oVTA logo, PLUS the Mesa Tech logo (under the text "Hosted by"), QFRA logo (under the text "Technically co-sponsored by") -- see the attached files. Where multiple versions of the logo have been supplied, you may select any version to use;

5. be able to be easily adapted by the Special Track Chairs to create their own Calls for Papers and Proposals using the same layout and format, changing the color scheme and/or graphics to achieve differentiation from the main Call while ensuring it looks like it is part of the same conference.

Target Market(s)

Researchers, scientists, technologists, and business professionals with an interest in using virtual reality (VR), augmented reality (AR), mixed reality (MR) and other XR technologies to support immersive learning in a range of education, training, and other settings.

Requirements
Must have
• Graphics and/or iconography, but NO PHOTOGRAPHS
Nice to have
• Optionally incorporate into the design some iconography/graphics alluding to different application areas of XR for learning -- e.g., Medical/Health Education, Culture & Heritage, Workforce Development, Educational Assessment, Place-based Learning (Field Trips). However, please do not write out the names of these application areas in text anywhere in the design;
Should not have
• Photographs

```html
<!DOCTYPE html>
<html lang="en">
<head>
<meta charset="utf-8">
<title>oVTA 2020 Call for Papers &amp; Proposals</title>
<link rel="stylesheet" href="https://fonts.googleapis.com/css2?family=Oswald:wght@300;400;500&family=Source+Sans+3:ital,wght@0,400;0,600;0,700;1,400&display=swap">
<style>
:root{
  --slate:#3a4047;
  --slate-deep:#2f343a;
  --orange:#f5821f;
  --orange-deep:#e06d10;
  --white:#ffffff;
  --ink:#33383d;
  --rule:#d9d9d9;
  --row:#ececec;
  --page-bg:#e4e2df;
  --sky-top:#0f1f4a;
  --sky-bottom:#3d63a8;
}
*{box-sizing:border-box;margin:0;padding:0}
html,body{width:1022px;height:1200px;overflow:hidden;background:var(--page-bg)}
body{font-family:"Source Sans 3",Arial,sans-serif;color:var(--ink)}
.flyer{position:absolute;left:31px;top:15px;width:960px;height:1170px;background:var(--white);overflow:hidden;box-shadow:0 2px 8px rgba(0,0,0,.15)}

/* masthead */
.masthead{position:absolute;left:0;top:0;width:960px;height:370px;background:var(--slate)}
.masthead__brand{position:absolute;left:0;top:0;width:350px;height:370px;padding:30px 28px}
.brand{display:flex;align-items:center;gap:12px}
.brand__dot{width:40px;height:40px;border-radius:50%;background:var(--orange);flex:none}
.brand__name{font-family:"Source Sans 3",Arial,sans-serif;font-weight:600;font-size:25px;line-height:1.02;color:var(--orange)}
.masthead__title{margin-top:70px;font-family:"Oswald",Arial,sans-serif;font-weight:300;font-size:44px;line-height:1.08;color:var(--white);letter-spacing:.5px}
.masthead__date{margin-top:16px;font-family:"Oswald",Arial,sans-serif;font-weight:300;font-size:22px;color:var(--orange)}
.masthead__art{position:absolute;left:340px;top:0;width:620px;height:370px}
.masthead__art svg{display:block}
.masthead__theme{position:absolute;right:18px;top:16px;font-family:"Oswald",Arial,sans-serif;font-weight:500;font-size:18px;color:var(--white);letter-spacing:.2px}
.masthead__vision{position:absolute;left:80px;top:145px;font-family:"Oswald",Arial,sans-serif;font-weight:400;font-size:40px;color:var(--slate-deep);background:rgba(255,255,255,.92);padding:0 18px;border-radius:4px}

/* conference band */
.band{position:absolute;left:0;top:370px;width:960px;height:62px;background:var(--orange);text-align:center;color:var(--white);font-family:"Oswald",Arial,sans-serif;font-weight:500;font-size:19px;line-height:26px;padding-top:5px}

/* sidebar */
.sidebar{position:absolute;left:0;top:432px;width:350px;height:738px;background:var(--slate);color:var(--white);display:flex;flex-direction:column}
.sidebar__title{padding:20px 22px 0;font-family:"Oswald",Arial,sans-serif;font-weight:300;font-size:25px;line-height:1.14;color:var(--orange)}
.sidebar__sponsor{padding:9px 22px 0;font-size:15px;line-height:1.25}
.partners{display:flex;gap:26px;align-items:center;padding:11px 22px 0}
.partner{font-family:"Source Sans 3",Arial,sans-serif;font-weight:600;font-size:18px;color:#d7d9dc;line-height:1}
.formats-tab{margin-top:15px;width:380px;height:30px;background:var(--orange);font-family:"Oswald",Arial,sans-serif;font-weight:500;font-size:13.5px;line-height:30px;padding-left:22px;color:var(--white);position:relative;z-index:2;flex:none}
.stream{padding:9px 22px 0}
.stream__name{font-family:"Oswald",Arial,sans-serif;font-weight:300;font-size:16.5px;color:var(--orange);line-height:1.2}
.stream__note{font-size:13px;line-height:1.2;color:#e3e5e8}
.stream ul{list-style:none;margin-top:2px}
.stream li{font-size:13px;line-height:1.25;padding-left:12px;position:relative}
.stream li::before{content:"";position:absolute;left:1px;top:7px;width:4px;height:4px;border-radius:50%;background:var(--orange)}
.inquiries{margin-top:auto;width:350px;background:var(--orange);padding:10px 22px 12px;font-size:13px;line-height:1.3;color:var(--white);flex:none}
.inquiries em{font-style:italic;font-weight:600}

/* main column */
.main{position:absolute;left:372px;top:446px;width:568px;height:710px;overflow:hidden}
.intro{font-size:11.4px;line-height:1.3;text-align:justify}
.intro strong{font-weight:700}
.section{display:flex;gap:12px;margin-top:13px}
.section__icon{flex:none;width:40px;height:40px;border-radius:50%;background:var(--orange);display:flex;align-items:center;justify-content:center}
.section__head{font-family:"Oswald",Arial,sans-serif;font-weight:500;font-size:15px;color:var(--orange);line-height:1.1;margin-bottom:3px}
.section__body{font-size:11.4px;line-height:1.3;text-align:justify}
.dates{margin-top:14px;border-top:1px solid var(--rule)}
.dates__tab{display:inline-block;background:var(--orange);color:var(--white);font-family:"Oswald",Arial,sans-serif;font-weight:500;font-size:11px;padding:2px 10px;margin-top:6px}
.dates table{width:100%;border-collapse:collapse;font-size:9.6px;line-height:1.2}
.dates td{padding:3px 6px;border-bottom:1px solid var(--white);vertical-align:middle}
.dates tr:nth-child(odd) td{background:var(--row)}
.dates tr:nth-child(even) td{background:#f6f6f6}
.dates td.date{width:74px;text-align:right;color:var(--orange-deep);font-weight:700}
.dates small{font-size:7.6px;font-style:italic}
</style>
</head>
<body>
<article class="flyer">

  <header class="masthead">
    <div class="masthead__brand">
      <div class="brand">
        <span class="brand__dot"></span>
        <span class="brand__name">Open Virtual Teaching Alliance</span>
      </div>
      <h1 class="masthead__title">CALL FOR PAPERS<br>&amp; PROPOSALS</h1>
      <p class="masthead__date">June 21–25, 2020</p>
    </div>
    <div class="masthead__art">
      <svg width="620" height="370" viewBox="0 0 620 370" role="img" aria-label="Night seascape with a lighthouse keeper's house on a rocky point, its beam sweeping the sky">
        <defs>
          <linearGradient id="sky" x1="0" y1="0" x2="0" y2="1">
            <stop offset="0" stop-color="var(--sky-top)"/>
            <stop offset="1" stop-color="var(--sky-bottom)"/>
          </linearGradient>
          <linearGradient id="shore" x1="0" y1="0" x2="0" y2="1">
            <stop offset="0" stop-color="#f2c99a"/>
            <stop offset="1" stop-color="#e3a673"/>
          </linearGradient>
        </defs>
        <path d="M40 0 H620 V370 H10 Q60 180 40 0 Z" fill="url(#sky)"/>
        <path d="M300 370 Q420 300 620 320 V370 Z" fill="url(#shore)"/>
        <path d="M40 0 Q60 180 10 370 H0 Q48 180 28 0 Z" fill="var(--white)"/>
        <path d="M28 0 Q48 180 0 370 V0 Z" fill="var(--slate)"/>
      </svg>
      <p class="masthead__theme">HINDSIGHT, INSIGHT, &amp; FORESIGHT IN XR &amp; IMMERSIVE LEARNING</p>
      <p class="masthead__vision">VISION 20/20</p>
    </div>
  </header>

  <div class="band">
    oVTA 2020: 6TH INTERNATIONAL CONFERENCE OF THE OPEN VIRTUAL TEACHING ALLIANCE<br>
    SAN LUIS OBISPO, CALIFORNIA, USA
  </div>

  <aside class="sidebar">
    <h2 class="sidebar__title">VISION 20/20: HINDSIGHT, INSIGHT, &amp; FORESIGHT IN XR &amp; IMMERSIVE LEARNING</h2>
    <p class="sidebar__sponsor">Technically co-sponsored by the QFRA Education Society, with proceedings to be submitted for inclusion in QFRA Library</p>
    <div class="partners">
      <span class="partner">QFRA</span>
      <span class="partner">Mesa Tech</span>
    </div>
    <div class="formats-tab">CONTRIBUTION TYPES &amp; SESSION FORMATS</div>

    <section class="stream">
      <h3 class="stream__name">Academic Stream</h3>
      <p class="stream__note">(Refereed paper published in proceedings)</p>
      <ul>
        <li>Full paper (6-8 pages) for oral presentation</li>
        <li>Short paper (4-6 pages) for oral presentation</li>
        <li>Short paper (4-6 pages) for poster presentation</li>
        <li>Work-in-progress paper (2-4 pages)<br>for poster presentation</li>
        <li>Work-in-progress paper (2-4 pages)<br>for doctoral colloquium</li>
      </ul>
    </section>
    <section class="stream">
      <h3 class="stream__name">Practitioner Stream</h3>
      <p class="stream__note">(No paper – Refereed on the basis of abstract)</p>
      <ul>
        <li>Oral presentation</li>
        <li>Poster presentation</li>
        <li>Demo showcase</li>
      </ul>
    </section>
    <section class="stream">
      <h3 class="stream__name">Nontraditional Session Formats</h3>
      <p class="stream__note">(Extended abstract published in proceedings)</p>
      <ul>
        <li>Pre-conference workshop</li>
        <li>Special session</li>
        <li>Panel session</li>
      </ul>
    </section>

    <div class="inquiries">
      Inquiries regarding the oVTA 2020 conference should be directed to the Conference Secretariat at <em>conference@ovtalearn.org</em>.<br>
      General inquiries about oVTA may be sent to <em>info@ovtalearn.org</em>.
    </div>
  </aside>

  <main class="main">
    <p class="intro"><strong>The 6th International Conference of the Open Virtual Teaching Alliance (oVTA 2020) will be an innovative and interactive gathering for a burgeoning global network of researchers and practitioners collaborating to develop the scientific, technical, and applied potential of immersive learning.</strong> It is the premier scholarly event focusing on advances in the use of virtual reality (VR), augmented reality (AR), mixed reality (MR), and other extended reality (XR) technologies to support learners across the full span of learning—from K-12 through higher education to work-based, informal, and lifelong learning contexts. Scholars and professionals operating in formal education settings as well as those representing diverse industry sectors are invited to participate in the conference, where they will be able to share their research findings, experiences, and insights; network and establish partnerships to envision and shape the future of XR and immersive technologies for learning; and contribute to the emerging scholarly knowledge base on how these technologies can be used to create experiences that educate, engage, and excite learners.</p>

    <section class="section">
      <div class="section__icon">
        <svg width="24" height="20" viewBox="0 0 24 20" aria-hidden="true" fill="var(--white)"><circle cx="6" cy="5" r="3"/><circle cx="18" cy="5" r="3"/><circle cx="12" cy="7" r="3.4"/><path d="M0 17 Q6 8 12 13 Q18 8 24 17 Z"/><path d="M5 20 Q12 10 19 20 Z"/></svg>
      </div>
      <div>
        <h3 class="section__head">PROGRAM TRACKS</h3>
        <p class="section__body">In addition to the main conference track, a small number of Special Tracks will be offered that focus on specific topic areas of interest within the field of XR and immersive learning. Those interested in proposing/chairing their own tracks should see the separate Call for Special Track proposals on the oVTA website. The deadline for Special Track proposals is 2019-09-30.</p>
      </div>
    </section>

    <section class="section">
      <div class="section__icon">
        <svg width="20" height="22" viewBox="0 0 20 22" aria-hidden="true" fill="none" stroke="var(--white)" stroke-width="2"><rect x="2" y="1" width="14" height="19" rx="1"/><path d="M5 6h8M5 10h8M5 14h5"/></svg>
      </div>
      <div>
        <h3 class="section__head">PAPER/PROPOSAL SUBMISSION AND REVIEW</h3>
        <p class="section__body">Papers for the Academic Stream and proposals/extended abstracts for the Nontraditional Session Streams must be prepared in standard QFRA double-column format, and will be accepted only by electronic submission through the conference website, from which guidelines and templates are available. A blind peer-review process will be used to evaluate all submissions.</p>
      </div>
    </section>

    <section class="section">
      <div class="section__icon">
        <svg width="22" height="20" viewBox="0 0 22 20" aria-hidden="true" fill="var(--white)"><rect x="1" y="2" width="5" height="17"/><rect x="8" y="0" width="5" height="19"/><rect x="15" y="4" width="5" height="15" transform="rotate(-8 17 12)"/></svg>
      </div>
      <div>
        <h3 class="section__head">PUBLICATION, ABSTRACTING, AND INDEXING</h3>
        <p class="section__body">All accepted and registered papers in the Academic Stream that are presented at oVTA 2020 and all extended abstracts describing the nontraditional sessions presented at the conference will be published in the conference proceedings and submitted to the QFRA Library digital library. Content loaded into the library is made available by QFRA to its abstracting and indexing partners, including Northmere (IndexPoint, EngCite), Luminar Analytics (CPRI—part of Scholar Ledger) and others, for potential inclusion in their respective databases. In addition, authors of selected papers may be invited to submit expanded versions of their papers for consideration by a number of IndexPoint and Scholar Ledger-indexed journals.</p>
      </div>
    </section>

    <section class="dates">
      <span class="dates__tab">IMPORTANT DATES</span>
      <table>
        <tr><td>Paper and proposal submission deadline <small>(Main round – all submission types welcome)</small></td><td class="date">2020-01-06</td></tr>
        <tr><td>Notification of review outcomes from main submission round</td><td class="date">2020-03-23</td></tr>
        <tr><td>Camera-ready papers for proceedings due – Full and Short papers</td><td class="date">2020-04-06</td></tr>
        <tr><td>Presenter registration deadline – Full and Short papers</td><td class="date">2020-04-06</td></tr>
        <tr><td>Paper and proposal submission deadline<br><small>(Late round – Only work-in-progress papers, practitioner abstracts, and nontraditional session proposals will be considered)</small></td><td class="date">2020-03-30</td></tr>
        <tr><td>Notification of review outcomes from late submission round</td><td class="date">2020-04-27</td></tr>
        <tr><td>Camera-ready Work-in-Progress papers and extended abstracts for Nontraditional sessions for proceedings due;<br>Final versions of practitioner abstracts for conference program due</td><td class="date">2020-05-11</td></tr>
        <tr><td>Presenter registration deadline – Work-in-progress papers, practitioner sessions, and nontraditional sessions</td><td class="date">2020-05-11</td></tr>
        <tr><td>Conference opening</td><td class="date">2020-06-21</td></tr>
      </table>
    </section>
  </main>

</article>
</body>
</html>
```